Profesional personal website needs design and business card

I need a business card with my professional name as a logo "Marlo Vitality" for my business. I am a Wellness Coach, consultant and trainer. So it should be professional, wellness oriented and modern.

Target Market(s)

Private clients, governments, corporations. Luxury and high market.

Industry/Entity Type

Health And Wellness

Contact Information for Business Card

Marlo Vitality should be the logo

Colors

Designer to choose colors to be used in the design.

Requirements
Must have
• Marlo Vitality
• Name: Tomás Arribal
• Wellness Coach, Consultant & Trainer.
• Website: www.marlovitality.example
• Phone:
• Spain (+34) 612 480 397
• (USA) +1 (555) 318 2046
Nice to have
• The most important is the design of "Marlo Vitality", as this is going to be my personal brand logo. It should be professional, wellness, high end and actual.
Should not have
• no golds, no baroque style..

```html
<!DOCTYPE html>
<html lang="en">
<head>
<meta charset="utf-8">
<title>Marlo Vitality — Business Card</title>
<link rel="stylesheet" href="https://fonts.googleapis.com/css2?family=Tinos:ital,wght@0,400;1,400&display=swap">
<style>
  :root {
    --card-green: #103503;
    --lime: #8afc2c;
    --white: #ffffff;
  }
  html, body {
    margin: 0;
    padding: 0;
    width: 1200px;
    height: 604px;
    overflow: hidden;
    background: var(--card-green);
  }
  .card {
    position: relative;
    width: 1200px;
    height: 604px;
    background: var(--card-green);
    font-family: "Tinos", "Times New Roman", serif;
    overflow: hidden;
  }
  .card p, .card h1, .card h2 {
    position: absolute;
    margin: 0;
    font-weight: 400;
    line-height: 1;
    white-space: nowrap;
  }

  /* Brand name */
  .brand-dot {
    position: absolute;
    left: 672px;
    top: 178px;
    width: 40px;
    height: 40px;
    border: 4px solid var(--lime);
    border-radius: 50%;
    box-sizing: border-box;
  }
  .brand-line {
    color: var(--white);
    font-size: 110px;
    letter-spacing: 1px;
  }
  .brand-line--first { left: 740px; top: 150px; }
  .brand-line--second { left: 668px; top: 232px; }

  /* Contact block */
  .person-name {
    left: 60px;
    top: 301px;
    color: var(--white);
    font-style: italic;
    font-variant: small-caps;
    font-size: 66px;
    letter-spacing: 2px;
  }
  .role {
    left: 60px;
    top: 373px;
    color: var(--lime);
    font-variant: small-caps;
    font-size: 46px;
    letter-spacing: 3.5px;
  }
  .phone {
    left: 60px;
    color: var(--lime);
    font-size: 50px;
    letter-spacing: 1px;
  }
  .phone--spain { top: 425px; }
  .phone--usa { top: 479px; }
  .phone .country { font-variant: small-caps; }
  .website {
    left: 60px;
    top: 541px;
    color: var(--lime);
    font-size: 34px;
    letter-spacing: 1px;
  }
</style>
</head>
<body>
  <main class="card">
    <span class="brand-dot" aria-hidden="true"></span>
    <h1 class="brand-name" aria-label="Marlo Vitality">
      <span class="brand-line brand-line--first" style="position:absolute">Marlo</span>
      <span class="brand-line brand-line--second" style="position:absolute">Vitality</span>
    </h1>

    <h2 class="person-name">Tomás Arribal</h2>
    <p class="role">Wellness Coach, Consultant &amp; Trainer</p>
    <p class="phone phone--spain"><span class="country">Spain</span> (+34) 612 480 397</p>
    <p class="phone phone--usa"><span class="country">USA</span> +1 (555) 318 2046</p>
    <p class="website">www.marlovitality.example</p>
  </main>
</body>
</html>
```